Book cover needed for a major new book on emotional resilience

The book will be titled: 'Stone to Stream: from habit bound to builders of renewal - The guide for growing steady teams and institutions'
My websites are http://www.pathmorrow.com and http://www.lumbrava.org and I am http://en.wikiverse-sample.org/wiki/Martin_Okonedo_(uncertainty_scholar) ad expert in developing emotional resilience. My previous book was The Murky Dividend.
The premise of the book is to introduce brand new material which is the first ever methodology and strategy on how to develop emotional resilience across entire populations like organisations and companies or moving people from fear about change to finding flow through resilience.
The final design should communicate the fact that this is a strategy and methodology. That it is about developing people and entire organisations to be more resilient and who are able to deal with change better.
Target Market(s)
Consultants, Organisational development consultants, Human Resource professionals.

```html
<!DOCTYPE html>
<html lang="en">
<head>
<meta charset="utf-8">
<title>Stone to Stream – Book Cover</title>
<link rel="stylesheet" href="https://fonts.googleapis.com/css2?family=Rokkitt:wght@300;400&family=Dancing+Script:wght@500&family=Open+Sans:wght@400;600&display=swap">
<style>
  :root {
    --page-bg: #ffffff;
    --cover-bg: #ffffff;
    --cover-edge: #e4e4e4;
    --title-green: #3fae49;
    --subtitle-green: #7cc36f;
    --tagline-grey: #5f6062;
    --author-grey: #6d6e70;
    --wave-green: #cfe6b4;
    --wave-pale: #eef6e4;
    --mist-grey: #e9eaea;
  }
  * { box-sizing: border-box; margin: 0; padding: 0; }
  html, body {
    width: 1200px;
    height: 900px;
    overflow: hidden;
    background: var(--page-bg);
  }
  .cover {
    position: absolute;
    left: 330px;
    top: 35px;
    width: 551px;
    height: 835px;
    background: var(--cover-bg);
    border: 1px solid var(--cover-edge);
    overflow: hidden;
  }
  .title-block {
    position: absolute;
    right: 54px;
    top: 176px;
    text-align: right;
  }
  .book-title {
    font-family: "Rokkitt", Georgia, serif;
    font-weight: 300;
    font-size: 46px;
    line-height: 1;
    color: var(--title-green);
    letter-spacing: 1px;
    white-space: nowrap;
  }
  .book-title .connector {
    font-family: "Dancing Script", cursive;
    font-weight: 500;
    font-size: 30px;
    letter-spacing: 0;
    margin: 0 2px;
  }
  .book-subtitle {
    font-family: "Rokkitt", Georgia, serif;
    font-weight: 400;
    font-size: 15px;
    color: var(--subtitle-green);
    margin-top: 2px;
    white-space: nowrap;
  }
  .book-tagline {
    position: absolute;
    right: 53px;
    top: 256px;
    font-family: "Open Sans", Arial, sans-serif;
    font-weight: 600;
    font-size: 10.5px;
    letter-spacing: 0.2px;
    color: var(--tagline-grey);
    text-transform: uppercase;
    white-space: nowrap;
  }
  .cover-art {
    position: absolute;
    left: 0;
    top: 292px;
    width: 100%;
    height: 543px;
    background:
      radial-gradient(ellipse 70% 28% at 70% 22%, var(--wave-green) 0%, rgba(207,230,180,0) 70%),
      radial-gradient(ellipse 60% 30% at 20% 40%, var(--wave-pale) 0%, rgba(238,246,228,0) 75%),
      linear-gradient(180deg, rgba(255,255,255,0) 0%, var(--wave-pale) 22%, var(--mist-grey) 52%, #f6f6f6 78%, #ffffff 100%);
  }
  .author {
    position: absolute;
    right: 46px;
    bottom: 38px;
    font-family: "Open Sans", Arial, sans-serif;
    font-weight: 400;
    font-size: 12.5px;
    letter-spacing: 0.4px;
    color: var(--author-grey);
    text-transform: uppercase;
  }
</style>
</head>
<body>
  <main class="cover">
    <div class="cover-art" role="img" aria-label="Flowing translucent green ribbons over a soft grey curved grid"></div>
    <header class="title-block">
      <h1 class="book-title">STONE <span class="connector">to</span> STREAM:</h1>
      <p class="book-subtitle">from habit bound to builders of renewal -</p>
    </header>
    <p class="book-tagline">The guide for growing steady teams &amp; institutions</p>
    <p class="author">Martin Okonedo</p>
  </main>
</body>
</html>
```